Quelmira Business Card

Need a business card for our business.

Attached are our Logos. There is either the white and black all the all red with white. Either Logo can be used.

The winner will be provided the details for phone number and address.

Good Luck!

Business

```html
<!DOCTYPE html>
<html lang="en">
<head>
<meta charset="utf-8">
<title>Quelmira Industries – Business Card</title>
<link rel="stylesheet" href="https://fonts.googleapis.com/css2?family=Cinzel:wght@400;600&family=Questrial&display=swap">
<style>
  :root {
    --stage: #1c1c1c;
    --card-black: #0b0b0b;
    --card-white: #ffffff;
    --brand-red: #8e1b1f;
    --ink: #222222;
    --ink-soft: #3a3a3a;
    --rule: #2a2a2a;
    --light-text: #e6e6e6;
  }
  * { margin: 0; padding: 0; box-sizing: border-box; }
  html, body {
    width: 1200px;
    height: 871px;
    overflow: hidden;
    background: var(--stage);
  }
  .canvas {
    position: relative;
    width: 1200px;
    height: 871px;
    display: flex;
    flex-direction: column;
    align-items: center;
    justify-content: space-evenly;
  }
  .card {
    position: relative;
    width: 640px;
    height: 366px;
    overflow: hidden;
  }

  /* Back side */
  .card--back {
    background: var(--card-black);
    display: flex;
    align-items: center;
    justify-content: center;
  }

  /* Brand wordmark */
  .brand {
    display: flex;
    align-items: center;
    gap: 12px;
  }
  .brand__mark {
    width: 18px;
    height: 18px;
    background: var(--brand-red);
  }
  .brand__name {
    font-family: "Questrial", sans-serif;
    font-weight: 400;
    color: var(--brand-red);
    letter-spacing: 0.08em;
    text-transform: uppercase;
  }
  .card--back .brand__name { font-size: 44px; }
  .card--back .brand__mark { width: 24px; height: 24px; }

  /* Front side */
  .card--front {
    background: var(--card-white);
    display: flex;
    flex-direction: column;
  }
  .front__body {
    flex: 1;
    display: flex;
    align-items: center;
    padding: 0 40px 0 46px;
  }
  .front__brand {
    width: 290px;
  }
  .front__brand .brand__name { font-size: 32px; }
  .front__brand .brand__rule {
    margin-top: 10px;
    width: 260px;
    height: 2px;
    background: var(--rule);
  }
  .front__details {
    margin-left: 30px;
    font-family: "Questrial", sans-serif;
    color: var(--ink-soft);
  }
  .person__name {
    font-family: "Cinzel", serif;
    font-weight: 600;
    font-size: 19px;
    letter-spacing: 0.12em;
    color: var(--ink);
  }
  .person__role {
    font-size: 13px;
    letter-spacing: 0.06em;
    color: var(--brand-red);
    margin-top: 2px;
  }
  .address {
    margin-top: 20px;
    font-size: 13.5px;
    line-height: 1.35;
    letter-spacing: 0.08em;
    font-style: normal;
  }
  .contact {
    margin-top: 14px;
    list-style: none;
    font-size: 13.5px;
    letter-spacing: 0.1em;
    line-height: 1.5;
  }
  .contact__item {
    display: flex;
    align-items: center;
    gap: 18px;
  }
  .contact__icon {
    width: 12px;
    height: 12px;
    fill: var(--brand-red);
  }
  .front__band {
    height: 64px;
    background: var(--card-black);
    display: flex;
    align-items: center;
    padding-left: 190px;
  }
  .website {
    font-family: "Questrial", sans-serif;
    font-size: 14px;
    letter-spacing: 0.2em;
    color: var(--light-text);
  }
</style>
</head>
<body>
<main class="canvas">
  <section class="card card--back" aria-label="Card back">
    <div class="brand">
      <span class="brand__mark"></span>
      <span class="brand__name">Quelmira Industries</span>
    </div>
  </section>

  <section class="card card--front" aria-label="Card front">
    <div class="front__body">
      <div class="front__brand">
        <div class="brand">
          <span class="brand__mark"></span>
          <span class="brand__name">Quelmira</span>
        </div>
        <div class="brand__rule"></div>
      </div>
      <div class="front__details">
        <p class="person__name">Dario Venn</p>
        <p class="person__role">Director</p>
        <address class="address">
          address<br>
          4321 first street<br>
          anytown, State ZIP
        </address>
        <ul class="contact">
          <li class="contact__item">
            <svg class="contact__icon" viewBox="0 0 12 12" aria-hidden="true">
              <path d="M1 4.5C1 2.5 3 1.5 6 1.5S11 2.5 11 4.5L9 5 8.5 3.8h-5L3 5Z"/>
              <rect x="2.5" y="6" width="7" height="5" rx="1"/>
            </svg>
            <span>123-456-7890</span>
          </li>
          <li class="contact__item">
            <svg class="contact__icon" viewBox="0 0 12 12" aria-hidden="true">
              <rect x="3" y="1" width="6" height="3"/>
              <rect x="1" y="4.5" width="10" height="4.5" rx="1"/>
              <rect x="3" y="8" width="6" height="3"/>
            </svg>
            <span>123-456-7891</span>
          </li>
        </ul>
      </div>
    </div>
    <div class="front__band">
      <span class="website">www.quelmira.co</span>
    </div>
  </section>
</main>
</body>
</html>
```